label design for coffee bean packaging

Logo will be provided. Label design for package of coffee beans for a micro roasted coffee company. Need to have space to write in origin, weight with check box for 1/4, 1/2, 1lb. Need to have check boxes for Light, Medium, Dark. Creative unique label design with boarders and fun, modern design. Company name is Cedar Brook Roasting Company. See attached logo. I have source files for logo if needed for design.
Industry/Entity Type
Coffee Shop
Font styles to use
Other font styles liked:
- Montez, kautiva cyrillic, uniform bold
Colors
f78f20
faa54b
f37122
fece3e
acd036
Requirements
Must have
- logo included in the design

```html
<!DOCTYPE html>
<html lang="en">
<head>
<meta charset="utf-8">
<title>Cedar Brook Roasting Company – Coffee Label</title>
<link rel="stylesheet" href="https://fonts.googleapis.com/css2?family=Baloo+2:wght@700;800&family=Yellowtail&display=swap">
<style>
  :root{
    --backdrop:#fdebb3;
    --orange-deep:#f37122;
    --orange:#f78f20;
    --orange-light:#faa54b;
    --yellow:#fece3e;
    --green:#acd036;
    --brown:#5a2c12;
    --white:#ffffff;
  }
  *{margin:0;padding:0;box-sizing:border-box}
  html,body{width:1200px;height:955px;overflow:hidden;background:var(--backdrop)}
  .label{position:absolute;left:380px;top:27px;width:440px;height:900px;overflow:hidden;
    box-shadow:0 6px 24px rgba(90,44,18,.18)}
  .label-art{position:absolute;inset:0}
  .brand-seal{position:absolute;left:137px;top:187px;width:166px;height:166px;border-radius:50%;
    background:var(--white);border:5px solid var(--brown);display:flex;align-items:center;
    justify-content:center;text-align:center;padding:18px}
  .brand-name{font-family:"Baloo 2",sans-serif;font-weight:700;font-size:19px;line-height:1.05;color:var(--brown)}
  .tagline{position:absolute;left:48px;width:344px;top:414px;text-align:center;
    font-family:"Baloo 2",sans-serif;font-weight:800;font-size:42px;color:var(--brown);letter-spacing:.5px;line-height:1}
  .product{position:absolute;left:48px;width:344px;top:476px;text-align:center;
    font-family:"Yellowtail",cursive;font-size:108px;line-height:1;color:var(--yellow)}
  .origin-badge{position:absolute;left:22px;top:616px;width:150px;height:150px}
  .origin-text{position:absolute;left:22px;top:616px;width:150px;height:150px;display:flex;align-items:center;
    justify-content:center;font-family:"Yellowtail",cursive;font-size:36px;color:var(--brown);transform:rotate(-14deg)}
  .options{position:absolute;left:48px;top:790px;width:344px;height:92px;background:var(--white);
    display:grid;grid-template-columns:1fr 1.2fr 1fr;grid-auto-rows:26px;row-gap:14px;padding:13px 14px;
    font-family:"Baloo 2",sans-serif;font-weight:700;font-size:18px;line-height:1;color:var(--brown)}
  .option{display:flex;align-items:center;gap:9px;height:26px;white-space:nowrap}
  .box{width:24px;height:24px;border:2px solid var(--brown);position:relative;flex:none}
  .box svg{position:absolute;left:1px;top:-10px}
</style>
</head>
<body>
<main class="label">
  <svg class="label-art" viewBox="0 0 440 900" width="440" height="900">
    <defs>
      <linearGradient id="orangeField" x1="0" y1="0" x2="1" y2="1">
        <stop offset="0" stop-color="#fbb23a"/>
        <stop offset=".45" stop-color="#f78f20"/>
        <stop offset="1" stop-color="#f05a22"/>
      </linearGradient>
      <linearGradient id="beanField" x1="0" y1="0" x2="0" y2="1">
        <stop offset="0" stop-color="#8a5026"/>
        <stop offset="1" stop-color="#5a2c12"/>
      </linearGradient>
    </defs>
    <rect width="440" height="900" fill="url(#orangeField)" role="img" aria-label="Faceted low-poly orange and yellow background"/>
    <path d="M113 0 V362 Q113 382 93 382 H62 Q44 382 44 400 V900 H396 V400 Q396 382 378 382 H347 Q327 382 327 362 V0 Z"
          fill="var(--yellow)" stroke="var(--brown)" stroke-width="3"/>
    <rect x="122" y="0" width="196" height="320" fill="var(--brown)"/>
    <rect x="48" y="462" width="344" height="150" fill="var(--brown)"/>
    <path d="M0 700 Q60 670 130 690 T260 676 T440 682 V900 H0 Z" fill="url(#beanField)"
          role="img" aria-label="Heap of roasted coffee beans"/>
  </svg>

  <div class="brand-seal"><span class="brand-name">Cedar Brook<br>Roasting<br>Company</span></div>

  <p class="tagline">MICRO ROASTED</p>
  <p class="product">Coffee</p>

  <svg class="origin-badge" viewBox="0 0 150 150" aria-hidden="true">
    <polygon fill="var(--green)" stroke="var(--brown)" stroke-width="1.5"
      points="75,8 83,20 96,11 100,26 115,22 114,37 129,38 123,52 137,58 127,69 138,80 125,87 132,101 117,104 119,119 104,117 100,132 87,125 80,139 70,128 59,137 53,123 39,128 37,113 22,112 27,98 13,92 24,81 13,70 26,63 20,49 35,47 33,32 48,34 51,19 64,25"/>
  </svg>
  <span class="origin-text">Origin</span>

  <section class="options" aria-label="Roast and weight">
    <div class="option"><span class="box"></span>Light</div>
    <div class="option"><span class="box"></span>Medium</div>
    <div class="option"><span class="box"><svg width="26" height="32" viewBox="0 0 26 32"><path d="M3 19 L10 28 L24 2" fill="none" stroke="var(--brown)" stroke-width="3"/></svg></span>Dark</div>
    <div class="option"><span class="box"></span>1/4</div>
    <div class="option"><span class="box"><svg width="26" height="32" viewBox="0 0 26 32"><path d="M3 19 L10 28 L24 2" fill="none" stroke="var(--brown)" stroke-width="3"/></svg></span>1/2</div>
    <div class="option"><span class="box"></span>1lb</div>
  </section>
</main>
</body>
</html>
```